Update a high tech public relations agency website

Hi! I am looking for a nice, clean refresh of my website. The URL is: www.bluemarkcomms.example.

Here's what I'm hoping for:
*To be able to go in to the Wordpress site and change text by myself once the design is set.
*To be able to go in and create a blog.

Here are examples of designs that I like. I'd like to see something along these lines:
www.pindlequill.example
www.GiveOver.example
www.ByCrew.example
www.Steadymailer.example
www.PostGlean.example

Some other things to note that may help:
*No white text with black background.
*I'm open to different color schemes. I like blue, green and red.
Updates

Hi all, Thanks for your interest in this project. Couple of things to note: please use the subheads in blue for the text. I don't want to use inbound marketing as the lead in. The up front text should be High Tech and AdTech Public Relations. Results Driven Media Relations. Content Strategy. Also, please....no stock images of people smiling or shaking hands or doing other fake corporate activities. Graphics would be nice. Thank you.

Industry/Entity Type

Tech

```html
<!DOCTYPE html>
<html lang="en">
<head>
<meta charset="utf-8">
<title>Bluemark Communications</title>
<link rel="stylesheet" href="https://fonts.googleapis.com/css2?family=Gelasio:wght@400&family=Open+Sans:wght@400;600&family=Mulish:wght@400;700&display=swap">
<style>
:root{
  --navy:#123d75;
  --ink:#1a4a7c;
  --green:#9cbf0e;
  --green-dark:#6e8a05;
  --card-bg:#f2f2f2;
  --footer:#174c7c;
  --text:#1c1c1c;
}
*{margin:0;padding:0;box-sizing:border-box}
html,body{width:1091px;height:1200px;overflow:hidden;background:#fff}
body{position:relative;font-family:"Open Sans",sans-serif;color:var(--text)}
.site-header{position:absolute;left:0;top:0;width:1091px;height:100px;background:linear-gradient(#f4f4f4,#ececec);border-bottom:1px solid #dcdcdc}
.brand{position:absolute;left:138px;top:24px;color:var(--ink);line-height:1;font-family:"Open Sans",sans-serif}
.brand-name{font-size:30px;font-weight:600;letter-spacing:-.5px;display:block}
.brand-sub{font-size:14.5px;font-weight:400;letter-spacing:.2px;display:block;margin-top:3px;color:#3c5a7c}
.main-nav{position:absolute;left:374px;top:37px;display:flex;align-items:center;height:26px}
.main-nav a{font-size:15px;color:var(--ink);text-decoration:none;padding:0 9px;line-height:26px;border-radius:13px}
.main-nav a.is-active{background:var(--navy);color:#fff;padding:0 11px}
.social{position:absolute;left:872px;top:36px;display:flex;gap:2px}
.social span{width:26px;height:26px;display:block}
.social .s1{background:#1f9ee3}.social .s2{background:#2f4f8e}.social .s3{background:#bdbdbd;display:flex;align-items:center;justify-content:center}
.hero-title{position:absolute;left:0;width:1091px;top:164px;text-align:center;font-family:"Gelasio",serif;font-weight:400;font-size:31px;color:var(--ink);letter-spacing:-.6px}
.hero-graphic{position:absolute;left:306px;top:242px;width:478px;height:390px;border-radius:24px;background:radial-gradient(ellipse at 50% 70%,#a9d9f2 0%,#d6ebf7 40%,#eef4fa 70%,#fff 100%)}
.btn{position:absolute;top:640px;width:134px;height:34px;border-radius:17px;color:#fff;font-weight:600;font-size:14px;text-align:center;line-height:32px;text-decoration:none}
.btn-touch{left:139px;background:var(--navy);box-shadow:0 3px 0 #0a2750}
.btn-start{left:760px;background:var(--green);box-shadow:0 3px 0 var(--green-dark)}
.tagline{position:absolute;left:0;width:1080px;top:650px;text-align:center;font-family:"Mulish",sans-serif;font-size:14.5px;color:var(--ink)}
.section-title{position:absolute;left:0;width:1091px;top:748px;text-align:center;font-family:"Gelasio",serif;font-weight:400;font-size:34px;color:var(--ink);letter-spacing:-.8px}
.card{position:absolute;top:822px;width:267px;height:268px;border-top:6px solid var(--ink);background:radial-gradient(ellipse at 50% 45%,#fbfbfb,var(--card-bg) 80%);padding:0 28px 0 40px}
.card h3{font-family:"Gelasio",serif;font-weight:400;font-size:18.5px;line-height:22px;color:#1a1a1a}
.card p{font-size:11px;line-height:15.2px;margin-top:10px}
.card-1{left:137px}.card-1 h3{margin-top:45px}
.card-2{left:411px;padding-left:35px}.card-2 h3{margin-top:61px}
.card-3{left:687px;padding-left:33px}.card-3 h3{margin-top:58px}
.learn-more{position:absolute;left:35px;top:209px;width:77px;height:21px;border-radius:11px;background:var(--green);box-shadow:0 2px 0 var(--green-dark);color:#fff;font-size:10px;text-align:center;line-height:20px;text-decoration:none}
.site-footer{position:absolute;left:0;top:1146px;width:1091px;height:54px;background:var(--footer);color:#fff}
.footer-links{position:absolute;left:148px;top:14px;font-size:10px}
.footer-links a{color:#fff;text-decoration:none}
.phone{position:absolute;left:756px;top:10px;display:flex;align-items:center;gap:12px;font-size:27px;line-height:34px}
.phone-icon{width:23px;height:23px;border-radius:50%;background:#0b0b0b;display:flex;align-items:center;justify-content:center}
</style>
</head>
<body>
<header class="site-header">
  <div class="brand"><span class="brand-name">Bluemark</span><span class="brand-sub">COMMUNICATIONS</span></div>
  <nav class="main-nav">
    <a href="#">Home</a><a href="#" class="is-active">About Us</a><a href="#">What we do</a><a href="#">Principal</a><a href="#">Services</a><a href="#">Contact</a>
  </nav>
  <div class="social">
    <span class="s1"></span><span class="s2"></span>
    <span class="s3"><svg width="16" height="12" viewBox="0 0 16 12"><rect x=".5" y=".5" width="15" height="11" fill="#fff" stroke="#eee"/><path d="M.5 .5 8 7 15.5 .5" fill="none" stroke="#bdbdbd"/></svg></span>
  </div>
</header>

<h1 class="hero-title">High Tech Public Relations. Content Strategy.</h1>

<div class="hero-graphic" role="img" aria-label="Illustration of a cloud linked to service icons"></div>

<a class="btn btn-touch" href="#">GET IN TOUCH</a>
<p class="tagline">Lorem ipsum dolor sit amet, consectetur</p>
<a class="btn btn-start" href="#">GET STARTED</a>

<h2 class="section-title">About Us</h2>

<article class="card card-1">
  <h3>High Tech Public Relations</h3>
  <p>Partner with an independent public relations resource or our team of independent communications pros.</p>
  <p style="margin-top:15px">Each team member has a minimum of 15 years experience on both the</p>
  <a class="learn-more" href="#">Learn More</a>
</article>
<article class="card card-2">
  <h3>Media Relations</h3>
  <p style="margin-top:13px">Our strategic approach to media relations focuses on building long-term relationships with journalists and influencers. We partner with you to develop compelling business and industry stories.</p>
</article>
<article class="card card-3">
  <h3>Content Strategy</h3>
  <p style="margin-top:15px">BluemarkPR excels at writing quality content. This comes from a deep understanding of technology, digital marketing, and the challenges facing CMOs and CIOs. It results in jargon-free press releases and spot on pitches that</p>
</article>

<footer class="site-footer">
  <div class="footer-links"><a href="#">About Us</a> | <a href="#">Contact Us</a> | <a href="#">Terms &amp; Condition</a> &nbsp;| &nbsp;<a href="#">Privacy Policy</a> Copyright © 2014 Bluemark. All rights reserved</div>
  <div class="phone"><span class="phone-icon"><svg width="12" height="12" viewBox="0 0 24 24"><path fill="#fff" d="M6.6 10.8a15 15 0 0 0 6.6 6.6l2.2-2.2c.3-.3.7-.4 1-.2 1.1.4 2.3.6 3.6.6.6 0 1 .4 1 1V20c0 .6-.4 1-1 1A17 17 0 0 1 3 4c0-.6.4-1 1-1h3.5c.6 0 1 .4 1 1 0 1.3.2 2.5.6 3.6.1.3 0 .7-.2 1z"/></svg></span>555 014 2290</div>
</footer>
</body>
</html>
```